Tidewell Venture Group
TVG Tidewell Venture Group
THE ONLY CHECK YOU WILL WRITE, WILL BE SMALLER THEN THE ONE YOU WROTE THE MONTH BEFORE.
Corporate
We are looking for a brochure design with the attached logo.
The brochure should reflect the professional nature of what we do and the colors and look should flow with the logo.
Looking for a tri fold and book type design.
Use the vector file for the logo.

```html
<!DOCTYPE html>
<html lang="en">
<head>
<meta charset="utf-8">
<title>Tidewell Venture Group – Tri-fold Brochure</title>
<link href="https://fonts.googleapis.com/css2?family=Arimo:wght@400;700&display=swap" rel="stylesheet">
<style>
  :root{
    --bg:#e6e6e6;
    --paper:#ffffff;
    --ink:#1b1b1b;
    --brand-blue:#1f6fb0;
    --bar-top:#4a9ad6;
    --bar-bottom:#145a94;
    --tab-edge:#0d3f6a;
  }
  *{box-sizing:border-box;margin:0;padding:0}
  html,body{width:1200px;height:896px;overflow:hidden}
  body{background:var(--bg);font-family:"Arimo",Arial,sans-serif;color:var(--ink);position:relative}
  .brochure{position:absolute;left:71px;top:178px;width:1059px;height:560px;display:flex;gap:8px}
  .panel{background:var(--paper);height:100%;position:relative;overflow:hidden;box-shadow:0 2px 8px rgba(0,0,0,.25)}
  .panel--cover{width:330px}
  .panel--inside{width:356px}
  .panel--back{width:357px}

  /* cover */
  .brand{position:absolute;left:26px;top:30px;color:var(--brand-blue);font-weight:700}
  .brand__mark{display:flex;align-items:center;gap:10px;font-size:64px;line-height:1;letter-spacing:4px}
  .brand__square{width:18px;height:18px;background:var(--brand-blue)}
  .brand__name{font-size:19px;margin-top:6px}
  .cover__title{position:absolute;left:26px;top:140px;font-size:38px;font-weight:700;color:#222}
  .cover__photo{position:absolute;left:0;top:190px;width:330px;height:320px;
    background:linear-gradient(160deg,#f7f3ee 0%,#f3c9a0 40%,#e8792a 70%,#f6f6f6 100%)}
  .cover__foot{position:absolute;left:20px;top:516px;width:300px;font-size:8.5px;line-height:1.35;white-space:nowrap}

  /* shared */
  .bar{height:40px;border-radius:0 20px 20px 0;background:linear-gradient(var(--bar-top),var(--bar-bottom));
    border-left:10px solid var(--tab-edge);color:#fff;font-weight:700;font-size:23px;display:flex;align-items:center;padding-left:18px}
  .copy{font-size:9px;line-height:1.3;font-weight:700;overflow-wrap:anywhere}
  .copy p{margin-bottom:7px}

  /* inside */
  .inside__photo{position:absolute;left:90px;top:8px;width:174px;height:108px;
    background:linear-gradient(135deg,#ffffff 0%,#c9c9c9 45%,#2d2d2d 75%,#f1f1f1 100%)}
  .panel--inside .bar{position:absolute;left:16px;top:120px;width:300px}
  .panel--inside .copy{position:absolute;left:22px;top:172px;width:316px}

  /* back */
  .panel--back .bar{position:absolute;left:0;top:12px;width:336px;border-left:none;border-radius:0 20px 20px 0}
  .panel--back .copy{position:absolute;left:14px;top:62px;width:330px}
  .back__globe{position:absolute;left:0;top:330px;width:357px;height:230px;
    background:radial-gradient(circle at 60% 55%,#ffffff 0%,#9cc9ee 30%,#2d79c2 60%,#0e4a86 100%)}
  .back__photo{position:absolute;left:180px;top:318px;width:150px;height:70px;
    background:linear-gradient(180deg,#e9eef5 0%,#8a97a8 50%,#2f3a48 100%)}
</style>
</head>
<body>
<main class="brochure">
  <section class="panel panel--cover">
    <div class="brand">
      <div class="brand__mark"><span class="brand__square"></span>TVG</div>
      <div class="brand__name">Tidewell Venture Group</div>
    </div>
    <h1 class="cover__title">Our Services</h1>
    <div class="cover__photo" role="img" aria-label="Smiling businesswoman in an orange shirt beside a rising bar chart"></div>
    <p class="cover__foot">Marlo, http://www.vale-notes.net/~mvale/<br>Pages about Web authoring: http://www.vale-notes.net/~mvale/web.html</p>
  </section>

  <section class="panel panel--inside">
    <div class="inside__photo" role="img" aria-label="Two businessmen shaking hands across a desk"></div>
    <h2 class="bar">Business Solutions</h2>
    <div class="copy">
      <p>In some circumstances, maybe, to some people's eyes. To my eyes, with my choice of font, it makes things even worse by increasing spacing between letters, so that it is more difficult to recognize word borders since inter-word gap can be just a little wider than intra-word gaps.</p>
      <p>Beware that the results depend on the font face, canvas width, browser and its settings, and the phase of the moon, to mention a few things. Besides, implementations of justification are buggy. More info: http://www.vale-notes.net/~mvale/web/justify.html</p>
      <p>&gt; it's part of css3 specification.</p>
      <p>There is no CSS3 specification (yet). Just drafts and proposals.</p>
      <p>--<br>Marlo, http://www.vale-notes.net/~mvale/<br>Pages about Web authoring: http://www.vale-notes.net/~mvale/web.html</p>
      <p>In some circumstances, maybe, to some people's eyes. To my eyes, with my choice of font, it makes things even worse by increasing spacing between letters, so that it is more difficult to recognize word borders since inter-word gap can be just a little wider than intra-word gaps.</p>
      <p>Beware that the results depend on the font face, canvas width, browser and its settings, and the phase of the moon, to mention a few things. Besides, implementations of justification are buggy. More info: http://www.vale-notes.net/~mvale/web/justify.html</p>
    </div>
  </section>

  <section class="panel panel--back">
    <h2 class="bar">Services</h2>
    <div class="copy">
      <p>In some circumstances, maybe, to some people's eyes. To my eyes, with my choice of font, it makes things even worse by increasing spacing between letters, so that it is more difficult to recognize word borders since inter-word gap can be just a little wider than intra-word gaps.</p>
      <p>Beware that the results depend on the font face, canvas width, browser and its settings, and the phase of the moon, to mention a few things. Besides, implementations of justification are buggy. More info: http://www.vale-notes.net/~mvale/web/justify.html</p>
      <p>&gt; it's part of css3 specification.</p>
      <p>There is no CSS3 specification (yet).</p>
      <p>--<br>Marlo, http://www.vale-notes.net/~mvale/<br>Pages about Web authoring: http://www.vale-notes.net/~mvale/web.html</p>
    </div>
    <div class="back__globe" role="img" aria-label="Glowing blue globe with light streaks"></div>
    <div class="back__photo" role="img" aria-label="Group of business people joining hands over a table"></div>
  </section>
</main>
</body>
</html>
```